The Nine Gates for Tablet Reliance - Contemporary Book Cover Design

The Nine Gates for Tablet Reliance was published in March 2019 and is available on Brimora and other platforms now. However, I am not happy with the cover.  It's a good design in some ways - I thought it would stand out and be easily recognizable. But I don't really like the color scheme and feel that a self-help book should probably use some lighter colors and that the red is too strident. The color scheme carries over into other marketing materials like the website, social media, etc. and I don't like the red and black scheme for these purposes.
It's not essential that the cover contain an endorsement like the current one but it could. Here are some endorsements:
“A must-read for anyone who is addicted to or thinks they may have a problem with digital technology. This eloquent work will also be useful to academics and clinicians exploring potential solutions. The author recognizes the similarities between smartphone addiction and other addictions, and logically applies one of the most effective known solutions for addiction - The Nine Gates.”
-- Dale Wickersham: Noted Interventionist, Keynote Speaker and Addiction Visionary
“If you suffer from digital addiction, I strongly encourage you to use this book as your road map to get you back to the real world.”
-- Thomas Quillard, Founder of Online Channel Monitor.
The back cover would have the new design / color scheme, but can have similar text, bio, author image, etc. Or we could include the endorsements there and shorten the other text.
As for the cover it could be stylized, or an image, a partial image, or whatever. I am open to suggestions. Think about what would be inviting for a person searching for help with moderating their smartphone use.
Let's add a subtitle as well "An Inner Journey to Balanced Tablet Habits"
Here is a link to the book:
https://www.brimora.example/Nine-Gates-Tablet-Reliance/dp/4086213590

Target Market(s)
General, since this issue affects almost everyone.
Colors
Designer to choose colors to be used in the design.
Look and feel

```html
<!DOCTYPE html>
<html lang="en">
<head>
<meta charset="utf-8">
<title>The Nine Gates for Tablet Reliance – Book Cover Wrap</title>
<link rel="stylesheet" href="https://fonts.googleapis.com/css2?family=Jost:ital,wght@0,400;0,500;0,700;1,400;1,700&family=Arimo:wght@400&family=Roboto+Condensed:ital,wght@1,700&display=swap">
<style>
  :root {
    --page-bg: #ece7e0;
    --cover-top: #5c6377;
    --cover-mid: #3b4052;
    --cover-bottom: #262a37;
    --spine-shade: #2f3342;
    --ink-light: #ffffff;
    --ink-soft: #e9eaf0;
    --photo-violet: #7a4fc4;
    --photo-deep: #2b2247;
    --photo-skin: #7a5a48;
  }
  * { box-sizing: border-box; margin: 0; padding: 0; }
  html, body {
    width: 1200px; height: 800px; overflow: hidden;
    background: var(--page-bg);
  }
  .book-wrap {
    position: absolute; left: 104px; top: 50px;
    width: 992px; height: 700px;
    display: flex;
    box-shadow: 0 10px 30px rgba(0,0,0,.25);
  }
  .cover {
    position: relative; height: 100%;
    background: linear-gradient(180deg, var(--cover-top) 0%, var(--cover-mid) 45%, var(--cover-bottom) 100%);
    overflow: hidden;
  }
  .back-cover { width: 466px; padding: 46px 40px 0 40px; color: var(--ink-light); font-family: "Arimo", Arial, sans-serif; }
  .spine {
    width: 60px; height: 100%;
    background: linear-gradient(90deg, var(--spine-shade), var(--cover-mid) 50%, var(--spine-shade));
    position: relative; overflow: hidden;
  }
  .front-cover { width: 466px; }

  /* back cover */
  .back-title {
    font-family: "Jost", sans-serif; font-weight: 700;
    font-size: 17px; text-align: center; letter-spacing: .3px; text-transform: uppercase;
  }
  .back-subtitle {
    font-family: "Jost", sans-serif; font-weight: 400;
    font-size: 13px; text-align: center; text-transform: uppercase; line-height: 1.25;
    margin: 4px 40px 26px;
  }
  .back-copy { font-size: 11.2px; line-height: 1.32; color: var(--ink-soft); }
  .back-copy p { margin-bottom: 14px; }
  .back-copy .endorsement-late { margin-left: 120px; margin-top: 34px; }

  /* spine */
  .spine-text {
    position: absolute; left: 0; top: 0; width: 100%; height: 100%;
    writing-mode: vertical-rl;
    display: flex; justify-content: space-between; align-items: center;
    padding: 26px 0 24px;
    font-family: "Jost", sans-serif; color: var(--ink-light); text-transform: uppercase;
  }
  .spine-title { font-weight: 700; font-size: 15px; letter-spacing: .4px; }
  .spine-author { font-weight: 500; font-size: 15px; letter-spacing: .5px; }

  /* front photo area */
  .cover-photo {
    position: absolute; left: 40px; top: 110px; width: 360px; height: 590px;
  }
  .front-type {
    position: absolute; inset: 0; color: var(--ink-light);
    font-family: "Jost", sans-serif; text-transform: uppercase;
  }
  .front-title {
    position: absolute; top: 62px; left: 0; right: 0;
    text-align: center; font-weight: 700; line-height: .98;
    font-size: 58px; letter-spacing: -.5px;
    text-shadow: 0 2px 6px rgba(0,0,0,.3);
  }
  .front-title .small-word { font-size: 46px; }
  .front-subtitle {
    position: absolute; top: 420px; left: 30px; right: 30px;
    text-align: center; font-weight: 500; font-size: 17px; line-height: 1.15;
  }
  .front-endorsement {
    position: absolute; top: 545px; left: 36px; right: 30px;
    text-align: center; text-transform: none;
    font-weight: 400; font-size: 15px; line-height: 1.25;
  }
  .front-endorsement cite {
    display: block; margin-top: 4px;
    font-family: "Roboto Condensed", sans-serif; font-style: italic; font-weight: 700; font-size: 14px;
  }
  .front-author {
    position: absolute; bottom: 30px; left: 0; right: 0; text-align: center;
    font-weight: 500; font-size: 40px; letter-spacing: 11px;
  }
</style>
</head>
<body>
  <main class="book-wrap">
    <section class="cover back-cover">
      <h2 class="back-title">The Nine Gates for Tablet Reliance</h2>
      <p class="back-subtitle">An Inner Journey to Balanced<br>Tablet Habits</p>
      <div class="back-copy">
        <p>The Nine Gates for Tablet Reliance was published in March 2019 and is available on Brimora and other platforms now. However, I am not happy with the cover. It's a good design in some ways - I thought it would stand out and be easily recognizable. But I don't really like the color scheme and feel that a self-help book should probably use some lighter colors and that the red is too strident. The color scheme carries over into other marketing materials like the website, social media, etc. and I don't like the red and black scheme for these purposes.</p>
        <p>“A must-read for anyone who is addicted to or thinks they may have a problem with digital technology. This eloquent work will also be useful to academics and clinicians exploring potential solutions. The author recognizes the similarities between smartphone addiction and other addictions, and logically applies one of the most effective known solutions for addiction - The Nine Gates.”</p>
        <p>“If you suffer from digital addiction, I strongly encourage you to use this book as your road map to get you back to the real world.”<br>-- Thomas Quillard, Founder of Online Channel Monitor.</p>
        <p>The back cover would have the new design / color scheme, but can have similar text, bio, author image, etc. Or we could include the endorsements there and shorten the other text.</p>
        <p class="endorsement-late">“A must-read for anyone who is addicted to or thinks they may have a problem with digital technology. This eloquent work will also be useful to academics and clinicians exploring potential solutions. The author recognizes the similarities between smartphone addiction and other addictions, and logically applies one of the most effective known solutions for addiction - The Nine Gates.”<br>-- Dale Wickersham: Noted Interventionist, Keynote Speaker and Addiction Visionary</p>
      </div>
    </section>

    <section class="spine">
      <div class="spine-text">
        <span class="spine-title">The Nine Gates for Tablet Reliance</span>
        <span class="spine-author">Jarek Solvane</span>
      </div>
    </section>

    <section class="cover front-cover">
      <svg class="cover-photo" viewBox="0 0 360 590" role="img" aria-label="Photo of a hand holding a phone with a glowing violet lock screen">
        <defs>
          <radialGradient id="screenGlow" cx="50%" cy="40%" r="60%">
            <stop offset="0%" stop-color="#b08ae8"/>
            <stop offset="45%" stop-color="#7a4fc4"/>
            <stop offset="100%" stop-color="#2b2247" stop-opacity="0"/>
          </radialGradient>
          <linearGradient id="handTone" x1="0" y1="0" x2="0" y2="1">
            <stop offset="0%" stop-color="#7a5a48" stop-opacity="0"/>
            <stop offset="60%" stop-color="#6a4c3e" stop-opacity=".55"/>
            <stop offset="100%" stop-color="#3a2c28" stop-opacity=".7"/>
          </linearGradient>
        </defs>
        <rect x="0" y="0" width="360" height="590" fill="url(#handTone)"/>
        <rect x="0" y="0" width="360" height="480" fill="url(#screenGlow)"/>
      </svg>

      <div class="front-type">
        <h1 class="front-title">
          <span class="small-word">The</span><br>
          Nine Gates<br>
          <span class="small-word">For</span><br>
          Tablet<br>
          Reliance
        </h1>
        <p class="front-subtitle">An Inner Journey to Balanced<br>Tablet Habits</p>
        <blockquote class="front-endorsement">
          If you suffer from digital addiction, I strongly encourage you to use this book as your road map to get you back to the real world.
          <cite>-Thomas Quillard, Founder of Online Channel Monitor.</cite>
        </blockquote>
        <p class="front-author">Jarek Solvane</p>
      </div>
    </section>
  </main>
</body>
</html>
```